Design Banners for The Harbor Chapel

We are in need of a variety of professionally designed banners that are vibrant, fresh, and encouraging.
I have attached 2 logos, a QR code, and the current style guide.
We are moving locations to a much larger location and want it to look new and fresh.
We will need two Large (13-15ft) flag banners (2-sided) that will be out front to indicate the front entrance. These should be welcome banners and can be identical or can be complimentary.
We will need a retractable Welcome Banner (12 ft).
We will need a "Divider" Style banner that will be an intro on the road.
We will need retractable banner signs (6 feet) single-sided to be placed by children's church doors for check-in, infant to 2 years, 3 to 5 years, and 6 to 12 years.

We are looking for a wow factor, beautiful, vibrant, and inviting. The logo can be inverted. It is important that is specifically states The Harbor Chapel so that folks know it is a church.

I have also added some samples that we like...
Let me know any questions.

Target Market(s)

General Public

Industry/Entity Type

A Christian Church

Font styles to use
Other font styles liked:
• Please see included style guide.

Colors
59FF00
82FF00
B8FF75
E3FFCB
F4FFEA
F0912C
F2A743
F7CA91
FBE8D2
FDF5EE
EE7325
F08F49
F5BC92
FAE3D3
FDF4ED

Requirements
Must have
• Designs for signs and banners
Nice to have
• I have provided a copy of the current style guide including font and colors. If we could stay with oranges and greens, that would be great. But, open to fresh ideas.

```html
<!DOCTYPE html>
<html lang="en">
<head>
<meta charset="utf-8">
<title>The Harbor Chapel – Welcome Banner</title>
<link rel="stylesheet" href="https://fonts.googleapis.com/css2?family=Montserrat:wght@400;700&family=Parisienne&display=swap">
<style>
  :root {
    --page-bg: #ffffff;
    --banner-green: #86c38b;
    --banner-peach: #f4cfae;
    --banner-orange: #e8893a;
    --banner-dark: #1c110a;
    --ink: #111111;
    --mark-dark: #1e1e20;
  }
  html, body {
    margin: 0;
    padding: 0;
    width: 1200px;
    height: 962px;
    overflow: hidden;
    background: var(--page-bg);
  }
  .canvas {
    position: relative;
    width: 1200px;
    height: 962px;
  }
  .banner {
    position: absolute;
    left: 342px;
    top: 51px;
    width: 516px;
    height: 860px;
    overflow: hidden;
    background: var(--banner-green);
    box-shadow: 10px 14px 18px rgba(0,0,0,0.25);
    font-family: "Montserrat", sans-serif;
    color: var(--ink);
    text-align: center;
  }
  .worship-scene {
    position: absolute;
    left: 0;
    right: 0;
    top: 430px;
    bottom: 0;
    background:
      radial-gradient(ellipse 40% 30% at 50% 42%, rgba(255,244,220,0.9), rgba(255,244,220,0) 70%),
      linear-gradient(to bottom,
        rgba(134,195,139,1) 0%,
        var(--banner-peach) 25%,
        #f1a96b 48%,
        var(--banner-orange) 62%,
        #5a2e12 78%,
        var(--banner-dark) 88%,
        #000000 100%);
  }
  .brand {
    position: absolute;
    top: 152px;
    left: 0;
    right: 0;
    display: flex;
    justify-content: center;
    align-items: center;
    gap: 14px;
  }
  .brand-dot {
    width: 34px;
    height: 34px;
    border-radius: 50%;
    background: var(--mark-dark);
  }
  .brand-name {
    font-family: "Montserrat", sans-serif;
    font-weight: 700;
    font-size: 34px;
    color: var(--mark-dark);
    letter-spacing: 0.5px;
  }
  .prayer-script {
    position: absolute;
    top: 328px;
    left: 0;
    right: 0;
    margin: 0;
    font-family: "Parisienne", cursive;
    font-weight: 400;
    font-size: 54px;
    line-height: 1.1;
  }
  .prayer-lines {
    position: absolute;
    top: 408px;
    left: 0;
    right: 0;
    margin: 0;
    font-weight: 700;
    font-size: 27px;
    line-height: 46px;
  }
  .web-address {
    position: absolute;
    top: 532px;
    left: 0;
    right: 0;
    margin: 0;
    font-size: 17px;
    font-weight: 400;
    letter-spacing: 3px;
  }
  .web-address strong { font-weight: 700; }
</style>
</head>
<body>
  <main class="canvas">
    <section class="banner">
      <div class="worship-scene" role="img" aria-label="Silhouetted raised hands of worshippers before a softly glowing cross at sunset with drifting leaves"></div>

      <div class="brand">
        <span class="brand-dot"></span>
        <span class="brand-name">The Harbor Chapel</span>
      </div>

      <h1 class="prayer-script">Lord, Anchor Me.</h1>
      <p class="prayer-lines">Lord, Anchor the Church.<br>Lord, Anchor the Nations.</p>
      <p class="web-address">www.<strong>harborchapel</strong>.church</p>
    </section>
  </main>
</body>
</html>
```